IT Professional Services Marketing Web Site

The Kovrel Associates new web site, need to look clean and modern, it has to give the feel of a professional IT consulting firm (something like white / clean background), the design need to be influenced by this site: http://www.trundavio.com/ .
The whole site is a one page, plus a link to a blog site, with the following sections:
1. Menu
2. Main Area
3. Our Company
4. What we do
5. Our Clients
6. Our People
7. Events
8. Contact Us
The new web site will be hosted on WordPress
Updates

Target Market(s)

Project Management Offices in Medium to Large Organisations

Industry/Entity Type

It Company

Number of Pages Required

1 page

Font styles to use
Serif
Sans Serif

Requirements
Must have
• Implemented on WordPress
Nice to have
• Shadows on the images and areas to give the site a bit of depth

```html
<!DOCTYPE html>
<html lang="en">
<head>
<meta charset="utf-8">
<title>Kovrel Associates — Successful Business Intelligence</title>
<link rel="stylesheet" href="https://fonts.googleapis.com/css2?family=Oswald:wght@400;500;600&family=Open+Sans:wght@300;400;600;700&family=Merriweather:wght@400;700&display=swap">
<style>
:root{
  --blue:#1aaee6;
  --orange:#f26a1b;
  --ink:#3d3d3d;
  --grey:#6a6a6a;
  --dark:#1e1e1e;
  --darker:#141414;
  --white:#ffffff;
}
*{margin:0;padding:0;box-sizing:border-box}
html,body{width:1200px;height:4091px;overflow:hidden}
body{font-family:"Open Sans",Arial,sans-serif;color:var(--ink);background:var(--white);position:relative}
.section{position:absolute;left:0;width:1200px}
.abs{position:absolute}
.heading{font-family:"Oswald",Impact,sans-serif;font-weight:600;text-align:center;color:var(--ink);line-height:1;position:absolute;width:1200px;left:0}

/* hero */
.hero{top:0;height:783px;background:radial-gradient(ellipse at 50% 40%,#ffffff 0%,#f5f5f5 55%,#e7e7e7 100%)}
.brand{left:95px;top:50px;font-size:26px;font-weight:600;color:#4a4a4a;line-height:1}
.top-nav{left:409px;top:41px;width:693px;height:46px;border:1px solid #bdbdbd;background:#fff;display:flex;align-items:center;justify-content:space-around;padding:0 8px}
.top-nav a{font-size:12px;color:#555;text-decoration:none;padding:6px 6px}
.top-nav a.active{border-top:3px solid var(--orange);color:#333}
.hero-title{top:178px;width:1200px;text-align:center;font-size:46px;line-height:56px;font-weight:700;color:#555}
.hero-sub{top:234px;width:1200px;text-align:center;font-size:48px;line-height:60px;font-weight:300;color:#555}
.hero-tag{top:305px;width:1200px;text-align:center;font-size:23px;line-height:30px;font-weight:600;color:var(--blue);letter-spacing:1px}
.hero-art{left:382px;top:368px;width:436px;height:340px;border-radius:50% 50% 12px 12px;background:radial-gradient(circle at 50% 40%,#bfe8fb 0%,#d9f0fa 45%,#eef6fa 75%,rgba(238,246,250,0) 100%)}
.slide-arrow{top:408px;width:45px;height:45px}
.slide-arrow.prev{left:60px;background:var(--blue)}
.slide-arrow.next{left:1090px;background:var(--orange)}

/* bar */
.bar{top:783px;height:62px;background:var(--dark)}
.bar-name{left:97px;top:14px;font-size:30px;line-height:34px;color:#fff;font-weight:400}
.bar-nav{right:95px;top:23px;display:flex;gap:26px}
.bar-nav a{color:#fff;font-size:12px;font-weight:600;text-decoration:none}

/* company */
.company{top:845px;height:396px;background:#fff}
.company .heading{top:40px;font-size:72px}
.company-text{left:190px;top:124px;width:820px;text-align:center;font-size:13px;line-height:19px;color:#555}
.company-text p{margin-bottom:16px}
.company-text .lead{color:var(--blue);font-style:italic}

/* services */
.services{top:1241px;height:553px;background:var(--blue)}
.services .heading{top:40px;font-size:70px;color:#fff}
.service{top:136px;width:232px}
.service-img{width:232px;height:137px;border:4px solid #fff;background:linear-gradient(135deg,#e9eef2,#b8c6d2)}
.service h3{font-family:"Oswald",sans-serif;font-weight:600;color:#fff;font-size:21px;line-height:26px;margin-top:16px;text-transform:uppercase}
.service p{color:#fff;font-size:13px;line-height:19px;margin-top:6px}

/* what we do */
.whatwedo{top:1794px;height:892px;background:radial-gradient(ellipse at 50% 50%,#ffffff 0%,#f3f3f3 70%,#ececec 100%)}
.whatwedo .heading{top:47px;font-size:66px}
.feature-icon{width:176px;height:176px;border-radius:50%}
.feature h4{font-family:"Oswald",sans-serif;font-weight:500;font-size:23px;line-height:26px;color:#333}
.feature h5{font-family:"Oswald",sans-serif;font-weight:500;font-size:25px;line-height:28px;color:#333;margin-bottom:10px}
.feature p{font-size:12px;line-height:18px;color:#555}
.feature.right{text-align:right}

/* team */
.team{top:2686px;height:627px;background:#fff}
.team .heading{top:55px;font-size:66px}
.member{top:207px;width:229px}
.member-photo{position:relative;width:229px;height:257px;background:linear-gradient(180deg,#e4e4e4,#b9b9b9)}
.socials{position:absolute;right:8px;bottom:10px;display:flex;gap:4px}
.socials span{width:20px;height:20px;background:var(--blue);border:1px solid #fff}
.member-name{height:58px;padding:6px 12px;color:#fff;font-family:"Oswald",sans-serif;background:var(--blue)}
.member-name b{display:block;font-size:24px;font-weight:500;line-height:28px}
.member-name i{font-style:normal;font-size:11px}
.member.lead .member-name{background:var(--orange)}
.member p{font-size:11px;line-height:15px;color:#555;margin-top:10px}

/* clients */
.clients{top:3313px;height:327px;background:#fff}
.clients .heading{top:36px;font-size:66px}
.client-row{left:190px;top:157px;width:820px;display:flex;justify-content:space-between}
.client-row span{font-size:34px;color:#333;font-weight:400;letter-spacing:1px}
.client-row span.alt{color:var(--blue)}
.pager{top:256px;left:568px;display:flex;gap:10px}
.pager span{width:30px;height:30px;border-radius:50%;border:2px solid var(--blue);display:flex;align-items:center;justify-content:center}
.pager span.off{border-color:#ccc}

/* footer */
.footer{top:3640px;height:390px;background:var(--dark);color:#cfcfcf}
.footer h6{font-family:"Oswald",sans-serif;font-weight:500;color:#fff;font-size:24px;line-height:30px;letter-spacing:1px;margin-bottom:20px}
.col{top:30px}
.col-contact{left:95px;width:230px;font-family:"Merriweather",Georgia,serif;font-size:11px;line-height:22px}
.col-contact .org{font-size:15px;margin-bottom:14px;color:#e5e5e5}
.col-links{left:355px;width:230px}
.col-links li{list-style:none;font-family:"Merriweather",serif;font-size:11px;padding:7px 0;border-bottom:1px solid #2f2f2f;color:#9a9a9a}
.col-links li:first-child{color:#fff}
.col-tweets{left:611px;width:230px;font-family:"Merriweather",serif;font-size:11px;line-height:18px}
.tweet{margin-bottom:14px;color:#8c8c8c}
.tweet b{color:#fff}
.col-form{left:873px;width:230px}
.field{height:34px;background:#2a2a2a;margin-bottom:9px;padding:9px 10px;font-size:11px;color:#aaa}
.field.area{height:70px}
.submit{width:135px;height:34px;background:var(--blue);color:#fff;font-family:"Oswald",sans-serif;font-size:14px;display:flex;align-items:center;justify-content:center;letter-spacing:2px;margin-top:22px}

.legal{top:4030px;height:61px;background:var(--darker);color:#8a8a8a;font-size:11px}
.legal p{position:absolute;left:95px;top:22px}
</style>
</head>
<body>

<header class="section hero">
  <div class="abs brand">Kovrel Associates</div>
  <nav class="abs top-nav">
    <a class="active" href="#">Main Area</a><a href="#">Our Company</a><a href="#">Services graph</a><a href="#">What we do</a><a href="#">Our Clients</a><a href="#">Our People</a><a href="#">Events</a><a href="#">Contact Us</a>
  </nav>
  <h1 class="abs hero-title">Successful</h1>
  <h2 class="abs hero-sub">Business Intelligence.</h2>
  <p class="abs hero-tag">TURN YOUR DATA INTO RESULTS.</p>
  <div class="abs hero-art" role="img" aria-label="Illustration of a cloud connected to laptops and round business icons"></div>
  <div class="abs slide-arrow prev"><svg width="45" height="45" viewBox="0 0 45 45"><path d="M26 14 L18 22.5 L26 31" fill="none" stroke="#fff" stroke-width="3"/></svg></div>
  <div class="abs slide-arrow next"><svg width="45" height="45" viewBox="0 0 45 45"><path d="M19 14 L27 22.5 L19 31" fill="none" stroke="#fff" stroke-width="3"/></svg></div>
</header>

<div class="section bar">
  <div class="abs bar-name">Kovrel Associates</div>
  <nav class="abs bar-nav">
    <a href="#">Main Area</a><a href="#">Our Company</a><a href="#">Services graph</a><a href="#">What we do</a><a href="#">Our Clients</a><a href="#">Our People</a><a href="#">Events</a><a href="#">Contact Us</a>
  </nav>
</div>

<section class="section company">
  <h2 class="heading">OUR COMPANY</h2>
  <div class="abs company-text">
    <p class="lead">“Kovrel Associates is a specialist consulting company that focuses solely on the design, configuration, deployment, user training and support of Enterprise Project Management (EPM) solutions based upon Nortavia Plan Server and its supporting technologies. Kovrel Associates offers a true, end-to-end set of services for any organisation implementing an EPM solution within their business – to cover the lifecycle of that system.</p>
    <p>This 100% focus on Nortavia EPM systems means that the company has an in-depth of knowledge and experience that is unique in the local marketplace. Whether it's a complete implementation project, a hosted solution option, or on-going support for an existing system, Kovrel Associates have the services to meet its customers' needs.</p>
    <p>The team come from a diverse range of backgrounds including Engineering (Civil, Chemical and Systems), Project Management, and Software Development. A number have worked with Nortavia and Nortavia Consulting Services directly. Kovrel Associates continues to work closely with Nortavia to ensure awareness of latest product developments”</p>
  </div>
</section>

<section class="section services">
  <h2 class="heading">OUR SERVICES</h2>
  <div class="abs service" style="left:95px">
    <div class="service-img" role="img" aria-label="Photo of a smiling business team"></div>
    <h3>Lorem ipsum is simply a dummy text!</h3>
    <p>Lorem Ipsum is simply dummy text of the printing and typesetting industry. Lorem Ipsum has been the industry's standard dummy text ever since the 1500s, when an unknown printer took a galley of type and scrambled it to make a type specimen book.</p>
  </div>
  <div class="abs service" style="left:352px">
    <div class="service-img" role="img" aria-label="Photo of colleagues in a meeting"></div>
    <h3>Lorem ipsum is simply a dummy text!</h3>
    <p>Lorem Ipsum is simply dummy text of the printing and typesetting industry. Lorem Ipsum has been the industry's standard dummy text ever since the 1500s.</p>
  </div>
  <div class="abs service" style="left:609px">
    <div class="service-img" role="img" aria-label="Photo of a businessman leaping across a gap"></div>
    <h3>Lorem ipsum is simply a dummy text!</h3>
    <p>Lorem Ipsum is simply dummy text of the printing and typesetting industry. Lorem Ipsum has been the industry's standard dummy text ever since the 1500s, when an unknown printer.</p>
  </div>
  <div class="abs service" style="left:868px">
    <div class="service-img" role="img" aria-label="Photo of hands using a tablet"></div>
    <h3>Lorem ipsum is simply a dummy text!</h3>
    <p>Lorem Ipsum is simply dummy text of the printing and typesetting industry.</p>
  </div>
</section>

<section class="section whatwedo">
  <h2 class="heading">What We Do</h2>
  <div class="abs feature-icon" style="left:98px;top:142px;background:#4a4a4a">
    <svg width="176" height="176" viewBox="0 0 176 176"><path d="M88 56c-24 0-42 13-42 30 0 9 5 17 14 23l-5 17 19-10c5 1 9 2 14 2 24 0 42-14 42-32s-18-30-42-30z" fill="#fff"/></svg>
  </div>
  <div class="abs feature" style="left:305px;top:160px;width:405px">
    <h4>CONSULT</h4>
    <h5>FULLY CUSTOMIZABLE, FULLY FLEXABLE</h5>
    <p>Lorem Ipsum is simply dummy text of the printing and typesetting industry. Lorem Ipsum has been the industry's standard dummy text ever since the 1500s, when an unknown printer took a galley of type and scrambled it to make a type specimen book. It has survived not only five centuries, but also the leap into electronic typesetting, remaining essentially unchanged. It was popularised in the 1960s.</p>
  </div>
  <div class="abs feature right" style="left:490px;top:398px;width:405px">
    <h4>CLOUD</h4>
    <h5>FULLY CUSTOMIZABLE, FULLY FLEXABLE</h5>
    <p>Lorem Ipsum is simply dummy text of the printing and typesetting industry. Lorem Ipsum has been the industry's standard dummy text ever since the 1500s, when an unknown printer took a galley of type and scrambled it to make a type specimen book. It has survived not only five centuries, but also the leap into electronic typesetting, remaining essentially unchanged. It was popularised in the 1960s.</p>
  </div>
  <div class="abs feature-icon" style="left:916px;top:396px;background:var(--blue)">
    <svg width="176" height="176" viewBox="0 0 176 176"><path d="M62 110h58c12 0 20-8 20-18s-8-18-19-18c-2-14-14-24-28-24-12 0-22 7-26 18-11 0-20 9-20 21s7 21 15 21z" fill="#fff"/></svg>
  </div>
  <div class="abs feature-icon" style="left:98px;top:641px;background:var(--orange)">
    <svg width="176" height="176" viewBox="0 0 176 176"><path d="M108 52c-12 0-21 10-20 22l-38 38c-4 4-4 10 0 14s10 4 14 0l38-38c12 1 22-8 22-20l-12 10-12-4-4-12z" fill="#fff"/></svg>
  </div>
  <div class="abs feature" style="left:305px;top:642px;width:405px">
    <h4>CARE</h4>
    <h5>FULLY CUSTOMIZABLE, FULLY FLEXABLE</h5>
    <p>Lorem Ipsum is simply dummy text of the printing and typesetting industry. Lorem Ipsum has been the industry's standard dummy text ever since the 1500s, when an unknown printer took a galley of type and scrambled it to make a type specimen book. It has survived not only five centuries, but also the leap into electronic typesetting, remaining essentially unchanged. It was popularised in the 1960s.</p>
  </div>
</section>

<section class="section team">
  <h2 class="heading">Our Professional Team</h2>
  <div class="abs member lead" style="left:100px">
    <div class="member-photo" role="img" aria-label="Portrait photo of a team member in a suit"><div class="socials"><span></span><span></span><span></span></div></div>
    <div class="member-name"><b>Dorian Vale</b><i>developer</i></div>
    <p>Contrary to popular belief, Lorem Ipsum is not simply random text. It has roots in a piece of classical Latin literature from 45 BC, making it over 2000 years old.</p>
  </div>
  <div class="abs member" style="left:357px">
    <div class="member-photo" role="img" aria-label="Portrait photo of a team member lifting a dumbbell"><div class="socials"><span></span><span></span><span></span></div></div>
    <div class="member-name"><b>Marek Hollis</b><i>designer</i></div>
    <p>Contrary to popular belief, Lorem Ipsum is not simply random text. It has roots in a piece of classical Latin literature from 45 BC, making it over 2000 years old.</p>
  </div>
  <div class="abs member" style="left:614px">
    <div class="member-photo" role="img" aria-label="Portrait photo of a team member with glasses"><div class="socials"><span></span><span></span><span></span></div></div>
    <div class="member-name"><b>Tessa Brin</b><i>art director</i></div>
    <p>Contrary to popular belief, Lorem Ipsum is not simply random text. It has roots in a piece of classical Latin literature from 45 BC, making it over 2000 years old.</p>
  </div>
  <div class="abs member" style="left:871px">
    <div class="member-photo" role="img" aria-label="Portrait photo of a thoughtful team member"><div class="socials"><span></span><span></span><span></span></div></div>
    <div class="member-name"><b>Owen Carlo</b><i>ceo</i></div>
    <p>Contrary to popular belief, Lorem Ipsum is not simply random text. It has roots in a piece of classical Latin literature from 45 BC, making it over 2000 years old.</p>
  </div>
</section>

<section class="section clients">
  <h2 class="heading">Our Clients</h2>
  <div class="abs client-row">
    <span>Logo</span><span class="alt">LOGO</span><span>Logo</span><span>logo</span><span>Logo</span><span>LOGO</span><span>Logo</span>
  </div>
  <div class="abs pager">
    <span><svg width="12" height="12" viewBox="0 0 12 12"><path d="M8 2 L4 6 L8 10" fill="none" stroke="#1aaee6" stroke-width="2"/></svg></span>
    <span class="off"><svg width="12" height="12" viewBox="0 0 12 12"><path d="M4 2 L8 6 L4 10" fill="none" stroke="#bbb" stroke-width="2"/></svg></span>
  </div>
</section>

<footer class="section footer">
  <div class="abs col col-contact">
    <h6>CONTACT</h6>
    <div class="org">KOVREL ASSOCIATES</div>
    <div>Calderwick Office / Head Office</div>
    <div>Level 7, Suite 456 / 123 Ferrow Lane,</div>
    <div>Calderwick VIC 3099</div>
    <div>Phone 03 9120 5487</div>
    <div>Pellmoor Office</div>
    <div>Shop 6/223 Brannock Road,</div>
    <div>Pellmoor QLD 4188</div>
    <div>07 3140 5678</div>
  </div>
  <div class="abs col col-links">
    <h6>QUICK LINKS</h6>
    <ul>
      <li>• Lorem ipsum dolor sit</li>
      <li>• Amet consectetur</li>
      <li>• Praesent vel sem id</li>
      <li>• Curabitur hendrerit est</li>
      <li>• Aliquam eget erat nec sapien</li>
      <li>• Cras at augue nunc</li>
      <li>• Sed a nulla urna</li>
    </ul>
  </div>
  <div class="abs col col-tweets">
    <h6>LATEST TWEETS</h6>
    <div class="tweet"><b>@kovrelnews</b> Sed sit amet lorem phasellus pretium in tempus nulla aliquet tincidunt. Suspendisse lorem justo a nisl tellus vitae dolor. 1 day ago</div>
    <div class="tweet"><b>@kovrelnews</b> Sed sit amet lorem phasellus pretium in tempus nulla aliquet tincidunt. Suspendisse lorem justo a nisl tellus vitae dolor. 1 day ago</div>
  </div>
  <div class="abs col col-form">
    <h6>CONTACT US</h6>
    <div class="field">Full Name</div>
    <div class="field">Email Address</div>
    <div class="field">Subject</div>
    <div class="field area">Message</div>
    <div class="submit">SUBMIT</div>
  </div>
</footer>

<div class="section legal"><p>Copyright © 2015 Kovrel Associates · All Rights Reserved</p></div>

</body>
</html>
```